Informational Site for Advanced Chemistry R&D

The company develops oxidation chemistry for air, water, fuel pollution controls. The site has been prototyped at www.velmirlab.net. Take a look. Now, the task is to design it for eye-catching beauty with use of color, on-page scroll-driven color transition and parallax effects. Should capture the themes: high technology, wow it's beautiful, modern, uncluttered, clean urban environment.

Target Market(s)

China Environmentally Conscious Government and Industry,

Industry/Entity Type

It Company

Number of Pages Required

3 page

Font styles to use
Sans Serif

Requirements
Must have
• Parallax effects, desktop compatible, Rich, Modern, Simple, Graphic
Nice to have
• Mobile Phone Compatible
Should not have
• Flash, or anything that is slow to load or requires high bandwidth

```html
<!DOCTYPE html>
<html lang="en">
<head>
<meta charset="utf-8">
<title>VelmirLab — Advanced Oxidation Science</title>
<link rel="stylesheet" href="https://fonts.googleapis.com/css2?family=Open+Sans:wght@400;600;700&family=Noto+Serif:wght@700&display=swap">
<style>
:root{
  --teal:#2fbdb3;
  --teal-dark:#22a59c;
  --ink:#222;
  --white:#fff;
  --header-bg:#f2f2f2;
  --dark-panel:#1b2127;
  --icon-blue:#1a73b8;
  --tile-bg:#eef0f2;
  --link-blue:#1a73b8;
  --partners-bg:#ececec;
  --footer-blue:#1b6fb3;
  --footer-bottom:#155d98;
  --accent-red:#e0403a;
}
*{margin:0;padding:0;box-sizing:border-box}
html,body{width:1200px;height:3734px;overflow:hidden}
body{position:relative;font-family:"Open Sans",Arial,sans-serif;color:var(--ink);background:var(--white)}

/* header */
.site-header{position:absolute;left:0;top:0;width:1200px;height:115px;background:var(--header-bg)}
.brand{position:absolute;left:130px;top:36px;display:flex;align-items:center;gap:12px;font-size:26px;font-weight:700;color:var(--icon-blue)}
.brand-dot{width:34px;height:34px;border-radius:50%;background:var(--teal);flex:none}
.call{position:absolute;right:85px;top:40px;font-size:21px;display:flex;align-items:center;gap:10px}
.main-nav{position:absolute;left:0;top:115px;width:1200px;height:55px;background:var(--teal)}
.main-nav ul{list-style:none;position:absolute;left:410px;top:0;display:flex;height:55px}
.main-nav li{height:55px;line-height:55px;padding:0 25px;color:var(--white);font-size:16px;font-weight:600}
.main-nav li.active{background:var(--white);color:var(--ink);padding:0 22px;margin-right:24px}

/* hero */
.hero{position:absolute;left:0;top:170px;width:1200px;height:435px;background:linear-gradient(180deg,#1f2a33 0%,#4d5f6e 45%,#7a8894 60%,#3b4853 80%,#222c34 100%)}
.hero h1{position:absolute;left:0;right:0;top:135px;text-align:center;font-family:"Noto Serif",Georgia,serif;font-size:37px;line-height:51px;color:var(--white);letter-spacing:1px}
.slider-btn{position:absolute;top:178px;width:40px;height:40px;background:#111;display:flex;align-items:center;justify-content:center}

/* about */
.about{position:absolute;left:0;top:605px;width:1200px;height:505px;background:var(--teal)}
.section-title{text-align:center;font-weight:400}
.section-title::after{content:"";display:block;width:110px;height:3px;margin:6px auto 0;background:currentColor}
.about h2{position:absolute;left:0;right:0;top:30px;color:var(--white);font-size:40px}
.about p{position:absolute;left:108px;top:128px;width:560px;color:var(--white);font-size:15.5px;line-height:24px}
.read-more-btn{position:absolute;left:105px;top:370px;width:210px;height:34px;border:2px solid var(--white);transform:skewX(-20deg);color:var(--white);font-size:15px;display:flex;align-items:center;justify-content:center;gap:10px}
.read-more-btn span{transform:skewX(20deg);display:flex}
.photo-circle{position:absolute;border-radius:50%;border:5px solid var(--white)}

/* advanced oxidation */
.oxidation{position:absolute;left:0;top:1110px;width:1200px;height:385px;background:#f1f1f1}
.oxidation-diagram{position:absolute;left:40px;top:15px;width:460px;height:350px;background:radial-gradient(circle at 50% 50%,#f4d24a 0%,#f7e7a4 30%,#f1f1f1 70%)}
.oxidation-panel{position:absolute;left:0;top:0;width:1200px;height:385px;background:var(--dark-panel);clip-path:polygon(740px 0,1200px 0,1200px 385px,500px 385px)}
.oxidation h2{position:absolute;right:50px;top:40px;font-size:38px;font-weight:400;color:var(--white)}
.oxidation .copy{position:absolute;right:50px;top:102px;width:470px;text-align:right;color:var(--white);font-size:15px;line-height:23px}
.oxidation .copy strong{display:block;font-weight:700}
.oxidation .copy p+p{margin-top:12px}

/* new ideas */
.ideas{position:absolute;left:0;top:1495px;width:1200px;height:600px;background:linear-gradient(135deg,#3e5568 0%,#6e8598 40%,#8799a8 60%,#4b6275 100%)}
.ideas h2{position:absolute;left:0;right:0;top:25px;color:var(--white);font-size:40px}
.idea{position:absolute;width:520px;height:110px;color:var(--white)}
.idea .icon{position:absolute;left:0;top:0;width:82px;height:82px;border-radius:50%;background:var(--icon-blue);display:flex;align-items:center;justify-content:center}
.idea h3{position:absolute;left:110px;top:-4px;font-size:23px;font-weight:400}
.idea p{position:absolute;left:110px;top:38px;font-size:18px;line-height:27px;white-space:nowrap}

/* solutions bar */
.solutions-bar{position:absolute;left:0;top:2095px;width:1200px;height:315px;background:var(--teal)}
.solutions-bar h2{position:absolute;left:0;right:0;top:30px;color:var(--white);font-size:40px}
.solution-pill{position:absolute;top:150px;display:flex;align-items:center;gap:26px;color:var(--white);font-size:40px}
.solution-pill .ring{width:100px;height:100px;border:3px solid var(--white);border-radius:50%;display:flex;align-items:center;justify-content:center}

/* solutions grid */
.solutions-grid{position:absolute;left:0;top:2410px;width:1200px;height:640px;background:var(--white)}
.solutions-grid h2{position:absolute;left:0;right:0;top:25px;font-size:40px}
.solutions-grid h2::after{background:var(--teal)}
.tile{position:absolute;width:597px;height:255px;background:var(--tile-bg);overflow:hidden}
.tile .photo{position:absolute;inset:0}
.tile h3{position:absolute;left:25px;top:55px;font-size:27px;font-weight:400;line-height:42px}
.tile a{position:absolute;left:25px;font-size:23px;color:var(--link-blue);text-decoration:none;border-bottom:2px solid var(--link-blue)}

/* partners */
.partners{position:absolute;left:0;top:3050px;width:1200px;height:330px;background:var(--partners-bg)}
.partners h2{position:absolute;left:0;right:0;top:28px;font-size:40px}
.partners h2::after{background:var(--teal)}
.partner{position:absolute;top:130px;width:135px;height:135px}

/* footer */
.accent-line{position:absolute;left:0;top:3376px;width:1200px;height:8px;background:var(--accent-red)}
.site-footer{position:absolute;left:0;top:3384px;width:1200px;height:306px;background:var(--footer-blue);color:var(--white)}
.site-footer .about-blurb{position:absolute;left:85px;top:50px;width:330px}
.footer-brand{display:flex;align-items:center;gap:10px;font-size:26px;font-weight:700;margin-bottom:22px;margin-top:20px}
.footer-brand .brand-dot{background:var(--white)}
.about-blurb p{font-size:15.5px;line-height:24px}
.footer-col{position:absolute;top:55px}
.footer-col h4{font-size:19px;font-weight:600;margin-bottom:16px}
.footer-col li{list-style:none;font-size:15px;line-height:34px;display:flex;align-items:center;gap:9px}
.bullet-ring{width:11px;height:11px;border:1.5px solid var(--white);border-radius:50%}
.social-circle{width:30px;height:30px;border:2px solid var(--white);border-radius:50%}
.footer-bottom{position:absolute;left:0;top:3690px;width:1200px;height:44px;background:var(--footer-bottom);color:var(--white);font-size:13px;text-align:center;line-height:44px}
</style>
</head>
<body>

<header class="site-header">
  <div class="brand"><span class="brand-dot"></span>VelmirLab</div>
  <div class="call">
    <svg width="24" height="24" viewBox="0 0 24 24"><circle cx="12" cy="12" r="12" fill="#1b6fb3"/><path d="M8 6.5l2 .3 1 2.6-1.3 1.1a7 7 0 003.7 3.7l1.1-1.3 2.6 1 .3 2a1.5 1.5 0 01-1.6 1.4A10 10 0 016.6 8.1 1.5 1.5 0 018 6.5z" fill="#fff"/></svg>
    Call us now! 866-555-0142
  </div>
</header>

<nav class="main-nav">
  <ul>
    <li class="active">HOME</li>
    <li>OUR SERVICES</li>
    <li>BLOG</li>
    <li>TESTIMONIALS</li>
    <li>CONTACT</li>
  </ul>
</nav>

<section class="hero" role="img" aria-label="City skyline reflected on a river at dusk">
  <h1>ADVANCED OXIDATION<br>SCIENCE FOR ENVIRONMENTAL<br>POLLUTION MANAGEMENT</h1>
  <div class="slider-btn" style="left:18px"><svg width="14" height="18" viewBox="0 0 14 18"><path d="M10 2L3 9l7 7" stroke="#fff" stroke-width="3" fill="none"/></svg></div>
  <div class="slider-btn" style="right:10px"><svg width="14" height="18" viewBox="0 0 14 18"><path d="M4 2l7 7-7 7" stroke="#fff" stroke-width="3" fill="none"/></svg></div>
</section>

<section class="about">
  <h2 class="section-title">About Us</h2>
  <p>Velmir Lab develops advanced oxidation technologies and materials, which it licenses to Velmir Systems, China.<br>Velmir Systems is engaged in the sales, service and support of environmental solutions for industry and government. With offices in Shanghai, Beijing, Shijiazhuang, and Chengdu, Velmir Systems is among the most advanced and rapidly growing companies offering solutions for air, water and fuel environmental compliance.<br>Velmir Lab Corporation supports these solutions with research and development.</p>
  <div class="read-more-btn"><span>Read More</span><span><svg width="16" height="16" viewBox="0 0 16 16"><circle cx="8" cy="8" r="7.5" fill="#fff"/><path d="M6 4.5L9.5 8 6 11.5" stroke="#2fbdb3" stroke-width="2" fill="none"/></svg></span></div>
  <div class="photo-circle" role="img" aria-label="Industrial tower and pipework" style="left:880px;top:82px;width:265px;height:265px;background:radial-gradient(circle at 40% 35%,#c9d6e2,#7a8ea3 60%,#4f6275)"></div>
  <div class="photo-circle" role="img" aria-label="Plant interior with equipment" style="left:745px;top:155px;width:125px;height:125px;background:linear-gradient(135deg,#8ba7c0,#3f5a72)"></div>
  <div class="photo-circle" role="img" aria-label="Industrial tanks" style="left:775px;top:255px;width:180px;height:180px;background:linear-gradient(135deg,#a8b4bf,#5b6a77)"></div>
</section>

<section class="oxidation">
  <div class="oxidation-diagram" role="img" aria-label="Reaction diagram of hydroxyl radical pathways"></div>
  <div class="oxidation-panel"></div>
  <h2>Advanced Oxidation</h2>
  <div class="copy">
    <p>Advanced Oxidation refers to a variety of techniques employing the Hydroxyl Radical, an energetic, highly reactive cousin of the water molecule:</p>
    <p><strong>To add oxygen to inorganic molecules</strong><strong>To remove hydrogen from organic molecules</strong></p>
    <p>These transformations convert important industrial contaminants into reactive forms that can be captured or that disintegrate into harmless end products.</p>
  </div>
</section>

<section class="ideas" role="img" aria-label="Blurred laboratory glassware in blue tones">
  <h2 class="section-title">New Ideas For A Cleaner World</h2>
  <div class="idea" style="left:68px;top:150px"><div class="icon"><svg width="40" height="40" viewBox="0 0 40 40"><path d="M6 26h20l8-6" stroke="#fff" stroke-width="3" fill="none"/><circle cx="22" cy="14" r="6" fill="#fff"/></svg></div><h3>Environmental</h3><p>This is Pixelmoor's version of Lorem Ipsum.<br>Proin gravida nibh vel velit auctor aliquet.</p></div>
  <div class="idea" style="left:625px;top:150px"><div class="icon"><svg width="40" height="40" viewBox="0 0 40 40"><path d="M8 28h18l6-5" stroke="#fff" stroke-width="3" fill="none"/><path d="M20 20c-6-2-6-10 0-14 6 4 6 12 0 14z" fill="#fff"/></svg></div><h3>Nature's Most</h3><p>This is Pixelmoor's version of Lorem Ipsum.<br>Proin gravida nibh vel velit auctor aliquet.</p></div>
  <div class="idea" style="left:68px;top:300px"><div class="icon"><svg width="40" height="40" viewBox="0 0 40 40"><path d="M6 32V18l8 5v-5l8 5v-5l8 5V8h4v24z" fill="#fff"/></svg></div><h3>Pollution Control</h3><p>This is Pixelmoor's version of Lorem Ipsum.<br>Proin gravida nibh vel velit auctor aliquet.</p></div>
  <div class="idea" style="left:625px;top:300px"><div class="icon"><svg width="40" height="40" viewBox="0 0 40 40"><path d="M15 6h10M17 6v10l-9 16h24l-9-16V6" stroke="#fff" stroke-width="3" fill="none"/></svg></div><h3>Reactive Free</h3><p>This is Pixelmoor's version of Lorem Ipsum.<br>Proin gravida nibh vel velit auctor aliquet.</p></div>
  <div class="idea" style="left:68px;top:440px"><div class="icon"><svg width="40" height="40" viewBox="0 0 40 40"><rect x="10" y="6" width="20" height="28" rx="3" stroke="#fff" stroke-width="3" fill="none"/><path d="M15 14h10M15 20h10M15 26h6" stroke="#fff" stroke-width="2.5"/></svg></div><h3>Solutions Employing</h3><p>This is Pixelmoor's version of Lorem Ipsum.<br>Proin gravida nibh vel velit auctor aliquet.</p></div>
  <div class="idea" style="left:625px;top:440px"><div class="icon"><svg width="40" height="40" viewBox="0 0 40 40"><circle cx="20" cy="20" r="5" fill="#fff"/><circle cx="8" cy="10" r="4" fill="#fff"/><circle cx="32" cy="10" r="4" fill="#fff"/><circle cx="20" cy="34" r="4" fill="#fff"/><path d="M8 10l12 10 12-10M20 20v14" stroke="#fff" stroke-width="2.5"/></svg></div><h3>Radical</h3><p>This is Pixelmoor's version of Lorem Ipsum.<br>Proin gravida nibh vel velit auctor aliquet.</p></div>
</section>

<section class="solutions-bar">
  <h2 class="section-title">Solutions</h2>
  <div class="solution-pill" style="left:88px"><div class="ring"><svg width="34" height="46" viewBox="0 0 34 46"><path d="M17 2C10 14 3 22 3 30a14 14 0 0028 0c0-8-7-16-14-28z" fill="#fff"/></svg></div>Water</div>
  <div class="solution-pill" style="left:485px"><div class="ring"><svg width="50" height="40" viewBox="0 0 50 40"><path d="M4 12h28a6 6 0 10-6-6M4 22h38a6 6 0 11-6 6M4 32h20" stroke="#fff" stroke-width="3" fill="none" stroke-linecap="round"/></svg></div>Air</div>
  <div class="solution-pill" style="left:798px"><div class="ring"><svg width="46" height="46" viewBox="0 0 46 46"><path d="M8 40l8-14 6-2 12-12 6 2-12 14-4 6-14 8z" fill="#fff"/><path d="M34 12l6-6" stroke="#fff" stroke-width="3"/></svg></div>Fuel</div>
</section>

<section class="solutions-grid">
  <h2 class="section-title">Solutions</h2>
  <div class="tile" style="left:0;top:130px">
    <div class="photo" role="img" aria-label="Refinery columns against the sky" style="background:linear-gradient(180deg,#9fb0bf,#4c5966);clip-path:polygon(330px 0,597px 0,597px 255px,180px 255px)"></div>
    <h3>Fuel Oil<br>Desulfurization</h3><a style="top:140px">Read More ›</a>
  </div>
  <div class="tile" style="left:600px;top:130px">
    <div class="photo" role="img" aria-label="Worker handling chemical containers" style="background:linear-gradient(180deg,#d6dde4,#7f93a8);clip-path:polygon(350px 0,600px 0,600px 255px,180px 255px)"></div>
    <h3>Volatile Organic<br>Compunds (VOC)</h3><a style="top:140px">Read More ›</a>
  </div>
  <div class="tile" style="left:0;top:385px">
    <div class="photo" role="img" aria-label="Smokestacks emitting flue gas" style="background:linear-gradient(180deg,#6d7e90,#2d3846);clip-path:polygon(330px 0,597px 0,597px 255px,180px 255px)"></div>
    <h3 style="left:30px">Flue Gas<br>Scrubbing</h3><a style="top:140px;left:30px">Read More ›</a>
  </div>
  <div class="tile" style="left:600px;top:385px">
    <div class="photo" role="img" aria-label="Wastewater flowing from a drain pipe" style="background:linear-gradient(180deg,#7d7a5e,#b3a06a 60%,#55604a);clip-path:polygon(350px 0,600px 0,600px 255px,180px 255px)"></div>
    <h3>Wastewater<br>Treatment</h3><a style="top:140px">Read More ›</a>
  </div>
</section>

<section class="partners">
  <h2 class="section-title">Partners</h2>
  <div class="partner" style="left:200px;display:flex;align-items:center;gap:10px;width:190px;font-size:26px;font-weight:700;color:#1b6fb3"><span class="brand-dot"></span>VelmirLab</div>
  <div class="partner" role="img" aria-label="Partner badge" style="left:450px;border-radius:14px;background:#e8c630"></div>
  <div class="partner" role="img" aria-label="Partner badge" style="left:640px;border-radius:50%;background:#2f5fa4"></div>
  <div class="partner" role="img" aria-label="Partner badge" style="left:830px;border-radius:50%;background:#b8343a"></div>
</section>

<div class="accent-line"></div>
<footer class="site-footer">
  <div class="about-blurb">
    <div class="footer-brand"><span class="brand-dot"></span>VelmirLab</div>
    <p>Velmir Lab develops advanced oxidation technologies and materials. which it licenses to Velmir Systems, China.</p>
  </div>
  <div class="footer-col" style="left:450px"><h4>NAVIGATION</h4><ul>
    <li><span class="bullet-ring"></span>Home</li><li><span class="bullet-ring"></span>Technology</li><li><span class="bullet-ring"></span>Products</li><li><span class="bullet-ring"></span>Contact</li></ul></div>
  <div class="footer-col" style="left:675px"><h4>FOLLOW US</h4><ul>
    <li><span class="social-circle"></span>circlebook</li><li><span class="social-circle"></span>chirpline</li><li><span class="social-circle"></span>snapgrid</li><li><span class="social-circle"></span>worklink</li></ul></div>
  <div class="footer-col" style="left:935px;width:240px"><h4>CONTACT</h4><ul>
    <li style="align-items:flex-start;line-height:22px"><svg width="12" height="16" viewBox="0 0 12 16" style="margin-top:3px;flex:none"><path d="M6 0a6 6 0 00-6 6c0 4 6 10 6 10s6-6 6-10a6 6 0 00-6-6z" fill="#fff"/><circle cx="6" cy="6" r="2" fill="#1b6fb3"/></svg>Velmir Lab Corporation<br>Marren Ferry, New Jersey, U.S.A.</li>
    <li style="margin-top:10px"><svg width="16" height="12" viewBox="0 0 16 12"><rect width="16" height="12" rx="1" fill="#fff"/><path d="M1 1l7 6 7-6" stroke="#1b6fb3" stroke-width="1.5" fill="none"/></svg>info@velmirlab.net</li>
    <li><svg width="14" height="14" viewBox="0 0 24 24"><path d="M5 2l4 .5 2 5-2.5 2a12 12 0 006 6l2-2.5 5 2 .5 4A2.5 2.5 0 0119.5 22 19 19 0 012 4.5 2.5 2.5 0 015 2z" fill="#fff"/></svg>+1 908-555-0187</li></ul></div>
</footer>
<div class="footer-bottom">© 2015 VelmirLab | All rights reserved.</div>

</body>
</html>
```